R. Calloway Peril Counsel Business Card

I need a business card that incorporates a two divisions of my company into one business card. The main company or division is R. Calloway Peril Counsel. We have a secondary division of R. Calloway Peril Counsel call Calloway Freight Insurance. I would like this name to be listed as "A Division of R. Calloway Peril Counsel".

Target Market(s)

Customers looking for insurance for their business. WE target businesses with revenues over $5MM

Industry/Entity Type

Business Insurance

Contact Information for Business Card

Use the current logo, but make the R. Calloway Peril Counsel most prevelant over the Calloway Freight Insurance. Name, email, phone number and location

Colors
0054AA
0677BA
7BADD7
CADEEF
E8F1F8

Requirements
Must have
• my current logo
Nice to have
• would like to have "A Division of R. Calloway Peril Counsel" on the card

```html
<!DOCTYPE html>
<html lang="en">
<head>
<meta charset="utf-8">
<title>R. Calloway Peril Counsel – Business Card</title>
<link href="https://fonts.googleapis.com/css2?family=Cinzel:wght@500&family=Poppins:ital,wght@0,400;1,600&display=swap" rel="stylesheet">
<style>
  :root {
    --backdrop: #2b2b2d;
    --navy: #15133d;
    --navy-text: #1d1a4c;
    --silver: #d9dadd;
    --silver-light: #f4f4f6;
    --silver-dark: #a9abb1;
    --ink: #e6e7ea;
    --rule: #9c9db0;
  }
  * { margin: 0; padding: 0; box-sizing: border-box; }
  html, body {
    width: 1200px; height: 875px; overflow: hidden;
    background: var(--backdrop);
  }
  .canvas {
    position: relative; width: 1200px; height: 875px;
    display: flex; align-items: center; justify-content: center;
  }
  .card {
    position: relative; width: 1000px; height: 580px;
    border-radius: 28px; overflow: hidden;
    background: var(--navy);
    box-shadow: 0 20px 50px rgba(0,0,0,.45);
    color: var(--ink);
    font-family: "Poppins", sans-serif;
  }
  .card-art { position: absolute; inset: 0; }
  .brand-main {
    position: absolute; left: 50px; top: 78px;
    display: flex; align-items: center; gap: 22px;
  }
  .brand-mark {
    width: 92px; height: 92px;
    border: 3px solid var(--silver); background: transparent;
  }
  .brand-name {
    font-family: "Cinzel", serif; font-weight: 500;
    font-size: 38px; line-height: 1.1; color: var(--silver);
    width: 430px;
  }
  .contact { list-style: none; font-size: 19px; line-height: 1; }
  .contact li { display: flex; align-items: center; gap: 12px; margin-bottom: 14px; }
  .contact svg { width: 16px; height: 16px; flex: none; fill: var(--ink); }
  .main-contact { position: absolute; left: 620px; top: 180px; }
  .brand-division {
    position: absolute; left: 620px; top: 280px; width: 340px;
    font-family: "Cinzel", serif; font-weight: 500;
    font-size: 34px; line-height: 1.1; color: var(--silver);
  }
  .person { position: absolute; left: 62px; top: 250px; }
  .person-name {
    font-family: "Cinzel", serif; font-weight: 500;
    font-size: 32px; color: var(--silver-light); line-height: 1;
  }
  .person-title { font-size: 18px; margin-top: 6px; }
  .direct-contact { position: absolute; left: 62px; top: 333px; }
  .freight-contact { position: absolute; left: 62px; top: 425px; }
  .division-line {
    position: absolute; left: 60px; top: 528px;
    font-style: italic; font-weight: 600; font-size: 22px;
    color: var(--navy-text);
  }
</style>
</head>
<body>
<main class="canvas">
  <section class="card" aria-label="Business card">
    <svg class="card-art" viewBox="0 0 1000 580" width="1000" height="580" aria-hidden="true">
      <defs>
        <linearGradient id="silverBand" x1="0" y1="0" x2="1" y2="1">
          <stop offset="0" stop-color="#bfc0c5"/>
          <stop offset=".45" stop-color="#f4f4f6"/>
          <stop offset="1" stop-color="#a9abb1"/>
        </linearGradient>
      </defs>
      <line x1="580" y1="125" x2="1000" y2="125" stroke="var(--rule)" stroke-width="1.2"/>
      <line x1="600" y1="258" x2="965" y2="258" stroke="var(--rule)" stroke-width="1.2"/>
      <line x1="60" y1="408" x2="965" y2="408" stroke="var(--rule)" stroke-width="1.2"/>
      <rect x="0" y="245" width="22" height="62" fill="url(#silverBand)"/>
      <path d="M0 500 L650 500 L695 458 L1000 458 L1000 580 L0 580 Z" fill="url(#silverBand)"/>
    </svg>

    <div class="brand-main">
      <div class="brand-mark"></div>
      <div class="brand-name">R. Calloway Peril Counsel</div>
    </div>

    <ul class="contact main-contact">
      <li><svg viewBox="0 0 16 16"><path d="M3 1h3l1.5 4-2 1.3a9 9 0 0 0 4.2 4.2L11 8.5l4 1.5v3a2 2 0 0 1-2 2A12 12 0 0 1 1 3a2 2 0 0 1 2-2z"/></svg>770-555-0190 R. Calloway Main</li>
      <li><svg viewBox="0 0 16 16"><circle cx="8" cy="8" r="7"/></svg>www.RCallowayPerilCounsel.com</li>
    </ul>

    <div class="brand-division">Calloway Freight Insurance</div>

    <div class="person">
      <div class="person-name">Grant Whitley</div>
      <div class="person-title">Founder / CEO</div>
    </div>

    <ul class="contact direct-contact">
      <li><svg viewBox="0 0 16 16"><path d="M3 1h3l1.5 4-2 1.3a9 9 0 0 0 4.2 4.2L11 8.5l4 1.5v3a2 2 0 0 1-2 2A12 12 0 0 1 1 3a2 2 0 0 1 2-2z"/></svg>404-555-0187</li>
      <li><svg viewBox="0 0 16 16"><path d="M1 3h14v10H1z M1 3l7 6 7-6" stroke="#15133d" stroke-width="1"/></svg>Grant@RCallowayIns.com</li>
    </ul>

    <ul class="contact freight-contact">
      <li><svg viewBox="0 0 16 16"><path d="M3 1h3l1.5 4-2 1.3a9 9 0 0 0 4.2 4.2L11 8.5l4 1.5v3a2 2 0 0 1-2 2A12 12 0 0 1 1 3a2 2 0 0 1 2-2z"/></svg>770-555-0142 Trucking Main</li>
      <li><svg viewBox="0 0 16 16"><circle cx="8" cy="8" r="7"/></svg>www.CallowayFreightInsurance.com</li>
    </ul>

    <div class="division-line">A Division of R. Calloway Peril Counsel</div>
  </section>
</main>
</body>
</html>
```